Laundromat washing machine soap instructions poster

I own a laundromat and need a poster explaining to my customers how to load the soap, bleach and fabric softener into our washing machines. I tried to make a poster on canva but it looks terrible. My Laundromat is called "Tidal Lane" and would like my logo to also be on the poster for branding. I would like the poster to use my blue logo colors to match my brand identity.
Under the photo please include the following text:
" *Please place pods inside the washer"
Thanks

```html
<!DOCTYPE html>
<html lang="en">
<head>
<meta charset="utf-8">
<title>Tidal Lane – Where Does the Soap Go?</title>
<link href="https://fonts.googleapis.com/css2?family=Montserrat:wght@700;800;900&display=swap" rel="stylesheet">
<style>
  :root {
    --sky: #c9f2fc;
    --brand-blue: #1d9ee0;
    --deep-blue: #0b62ad;
    --navy: #0d3c78;
    --label-blue: #1789c8;
    --white: #ffffff;
    --pale-wave: #8fd0ee;
    --tray-grey: #6d6f72;
    --tray-light: #d9dbdc;
  }
  * { margin: 0; padding: 0; box-sizing: border-box; }
  html, body { width: 849px; height: 1200px; overflow: hidden; }
  body { font-family: "Montserrat", sans-serif; background: var(--white); }
  .poster { position: relative; width: 849px; height: 1200px; overflow: hidden; }
  .backdrop { position: absolute; inset: 0; }
  .brand {
    position: absolute; top: 70px; left: 0; width: 100%;
    display: flex; justify-content: center; align-items: center; gap: 12px;
  }
  .brand-dot { width: 30px; height: 30px; border-radius: 50%; background: var(--deep-blue); }
  .brand-name { font-weight: 800; font-size: 40px; color: var(--deep-blue); letter-spacing: 1px; }
  .headline {
    position: absolute; top: 168px; left: 0; width: 100%;
    text-align: center; font-weight: 900; font-size: 80px; line-height: 92px; letter-spacing: 1px;
  }
  .headline .line-dark { color: var(--navy); display: block; }
  .headline .line-light { color: var(--white); display: block; }
  .graphics { position: absolute; inset: 0; }
  .label {
    position: absolute; font-weight: 800; font-size: 37px; line-height: 47px; text-align: center;
  }
  .label-softener { left: 20px; top: 600px; width: 260px; color: var(--label-blue); }
  .label-bleach { left: 620px; top: 650px; width: 200px; color: var(--label-blue); }
  .label-detergent { top: 988px; color: var(--white); font-size: 38px; }
  .label-detergent.left { left: 22px; }
  .label-detergent.right { left: 585px; }
  .note {
    position: absolute; left: 36px; top: 1102px;
    font-weight: 800; font-size: 36px; color: var(--white);
  }
</style>
</head>
<body>
<div class="poster">
  <svg class="backdrop" width="849" height="1200" viewBox="0 0 849 1200" aria-hidden="true">
    <defs>
      <linearGradient id="topFill" x1="0" y1="0" x2="0" y2="1">
        <stop offset="0" stop-color="#c9f2fc"/>
        <stop offset="0.14" stop-color="#bdeefb"/>
        <stop offset="0.22" stop-color="#2ab3ec"/>
        <stop offset="0.45" stop-color="#0f8bd0"/>
      </linearGradient>
      <linearGradient id="bottomFill" x1="0" y1="0" x2="1" y2="1">
        <stop offset="0" stop-color="#24a9e8"/>
        <stop offset="1" stop-color="#0c55a3"/>
      </linearGradient>
    </defs>
    <rect width="849" height="1200" fill="url(#topFill)"/>
    <path d="M0 1200 V740 C200 700 420 760 600 790 C720 805 800 780 849 760 V1200 Z" fill="url(#bottomFill)"/>
    <path d="M0 405 C120 345 280 350 430 395 C580 440 720 470 849 415 V450 C720 500 570 470 430 430 C280 385 130 380 0 440 Z" fill="var(--pale-wave)"/>
    <path d="M0 440 C130 380 280 385 430 430 C570 470 720 500 849 450 V775 C800 795 720 815 600 800 C420 775 200 715 0 760 Z" fill="var(--white)"/>
    <path d="M0 730 C200 690 420 750 600 780 C720 797 800 772 849 752 V775 C800 795 720 815 600 800 C420 775 200 715 0 760 Z" fill="var(--pale-wave)"/>
  </svg>

  <div class="brand">
    <span class="brand-dot"></span>
    <span class="brand-name">TIDAL LANE</span>
  </div>

  <h1 class="headline">
    <span class="line-dark">WHERE DOES</span>
    <span class="line-light">THE SOAP GO?</span>
  </h1>

  <svg class="graphics" width="849" height="1200" viewBox="0 0 849 1200">
    <defs>
      <linearGradient id="lidShade" x1="0" y1="0" x2="0" y2="1">
        <stop offset="0" stop-color="#7a7c7f"/>
        <stop offset="1" stop-color="#65676a"/>
      </linearGradient>
      <linearGradient id="arrowBlue" x1="0" y1="0" x2="1" y2="1">
        <stop offset="0" stop-color="#2aa6e0"/>
        <stop offset="1" stop-color="#0b7cc3"/>
      </linearGradient>
      <marker id="arrowHead" viewBox="0 0 10 10" refX="5" refY="5" markerWidth="3.2" markerHeight="3.2" orient="auto">
        <path d="M0 0 L10 5 L0 10 Z" fill="#0b7cc3"/>
      </marker>
    </defs>

    <g class="dispenser-photo" role="img" aria-label="Photo of an open washer soap dispenser with four compartments: softener, bleach and two detergent trays">
      <rect x="270" y="371" width="308" height="350" rx="6" fill="url(#lidShade)"/>
      <rect x="143" y="688" width="549" height="353" rx="18" fill="url(#lidShade)"/>
      <rect x="262" y="728" width="316" height="258" rx="14" fill="var(--tray-light)"/>
    </g>

    <g class="arrows" fill="none" stroke="url(#arrowBlue)" stroke-width="22" stroke-linecap="round" marker-end="url(#arrowHead)">
      <path d="M150 728 C230 695 300 730 318 782"/>
      <path d="M709 728 C630 695 560 730 545 782"/>
      <path d="M132 888 C215 860 285 900 300 946"/>
      <path d="M763 895 C680 865 610 900 597 946"/>
    </g>

    <g class="icon-softener" fill="none" stroke="var(--label-blue)" stroke-width="6">
      <circle cx="141" cy="552" r="10"/>
      <circle cx="159" cy="563" r="10"/>
      <circle cx="159" cy="585" r="10"/>
      <circle cx="141" cy="596" r="10"/>
      <circle cx="123" cy="585" r="10"/>
      <circle cx="123" cy="563" r="10"/>
    </g>

    <path class="icon-bleach" d="M718 590 L748 640 L688 640 Z" fill="none" stroke="var(--label-blue)" stroke-width="6" stroke-linejoin="round"/>

    <g class="icon-detergent" fill="none" stroke="var(--white)" stroke-width="6" stroke-linecap="round">
      <path d="M84 928 L94 972 L134 972 L144 928"/>
      <path d="M114 930 V958"/>
      <path d="M690 928 L700 972 L740 972 L750 928"/>
      <path d="M708 930 V958 M720 930 V958 M732 930 V958"/>
    </g>
  </svg>

  <div class="label label-softener">FABRIC<br>SOFTENER</div>
  <div class="label label-bleach">BLEACH</div>
  <div class="label label-detergent left">DETERGENT</div>
  <div class="label label-detergent right">DETERGENT</div>

  <p class="note">*Please place pods inside the washer</p>
</div>
</body>
</html>
```